The Lantern and the Meadow: A Quiet Bloom Within Us

We need a book cover/spine and back cover for a multi author book called the Lantern and The Meadow: A Quiet Bloom Within Us. This will be a collection of stories from women who major transformational stories to tell. They embark on a voyage, find themselves in uncharted territory, find friends or allies and in the end find themselves back home to themselves. I want this book cover to feel fun of wonder, adventure, intrigue with a a dainty energy. I have uploaded some images for inspiration but not to use in the design because they are not images I have permission to use.

```html
<!DOCTYPE html>
<html lang="en">
<head>
<meta charset="utf-8">
<title>The Lantern and the Meadow — Book Cover</title>
<link href="https://fonts.googleapis.com/css2?family=DM+Serif+Display&family=Oswald:wght@400&display=swap" rel="stylesheet">
<style>
  :root {
    --backdrop: #31204a;
    --sky-top: #6fa6c4;
    --sky-mid: #b9d3e0;
    --horizon: #9fb49a;
    --meadow: #6e8f4f;
    --meadow-deep: #3f5e2c;
    --lupine: #6a5fa8;
    --title: #ffffff;
  }
  html, body {
    margin: 0;
    padding: 0;
    width: 1200px;
    height: 1200px;
    overflow: hidden;
    background: var(--backdrop);
  }
  .book-cover {
    position: absolute;
    left: 282px;
    top: 138px;
    width: 636px;
    height: 953px;
    overflow: hidden;
    box-shadow: 0 18px 40px rgba(0, 0, 0, 0.35);
  }
  .cover-photo {
    position: absolute;
    inset: 0;
    background:
      radial-gradient(ellipse 40% 30% at 30% 80%, rgba(106, 95, 168, 0.45), transparent 70%),
      radial-gradient(ellipse 30% 25% at 85% 72%, rgba(106, 95, 168, 0.4), transparent 70%),
      linear-gradient(180deg,
        var(--sky-top) 0%,
        var(--sky-mid) 30%,
        #dfe8ea 44%,
        var(--horizon) 46%,
        var(--meadow) 60%,
        var(--meadow-deep) 100%);
  }
  .title {
    position: absolute;
    right: 30px;
    margin: 0;
    font-family: "DM Serif Display", Georgia, serif;
    font-weight: 400;
    color: var(--title);
    text-align: right;
    font-size: 118px;
    line-height: 0.84;
    letter-spacing: -2px;
  }
  .title span { display: block; }
  .title-top { top: 30px; }
  .title-bottom { top: 468px; }
  .subtitle {
    position: absolute;
    right: 32px;
    top: 872px;
    margin: 0;
    font-family: "Oswald", "Arial Narrow", sans-serif;
    font-weight: 400;
    font-size: 34px;
    letter-spacing: -0.5px;
    color: var(--title);
  }
</style>
</head>
<body>
  <div class="book-cover">
    <div class="cover-photo" role="img" aria-label="Photograph of a woman in a pale blue dress, seen from behind, carrying pink and white peonies through a green meadow of purple lupines under a cloudy blue sky"></div>
    <h1 class="title title-top"><span>The</span><span>Lantern</span></h1>
    <p class="title title-bottom"><span>and</span><span>The</span><span>Meadow</span></p>
    <p class="subtitle">A Quiet Bloom Within Us</p>
  </div>
</body>
</html>
```